Sports Nutrition line needs new label look/feel

We need a new label design for "Telmo",our Sports Nutrition line of vitamins, nutraceuticals, protein powders, and performance endurance products. We would like to see two separate designs, one blue and one red, as these are the two colors we are torn between. The labels should have the look/feel of a sports or fitness label, bold coloring, lettering, and even some use of holographic foiling.
Brands we would be similar to those found on pulsevaultshop.com and stridecraftnow.com. Brands we like in particular are QRT and Velmot.

Target Market(s)

Fitness enthusiasts,athletes, health nuts..

Industry/Entity Type

Nutrition

Font styles to use
Sans Serif
Decorative
Script

Colors
ec1f27
0692cd
0355a3
3276b5
f04a50

Requirements
Must have
• -Fitness look/feel
• -bold colors (preferably red and blue)
• -use of icons (eye health, brain, health, etc.)
• -"Fit" in "TelMO" must stand out
• -use tagline "Shaping Stronger Bodies"
Nice to have
• -holographic foiling elements
• -try to incorporate a molecular element (like those shown in the example labels)
Should not have
• -Light, calming colors
• -difficult to read fonts

```html
<!DOCTYPE html>
<html lang="en">
<head>
<meta charset="UTF-8">
<title>TelMO Power Nutrition Label</title>
<link rel="stylesheet" href="https://fonts.googleapis.com/css2?family=Signika:wght@500;600;700&display=swap">
<style>
  :root {
    --page: #ffffff;
    --label-black: #0c0c0c;
    --black-glow: #2f2f2f;
    --mesh-dark: #1a1a1a;
    --mesh-light: #4a4a4a;
    --silver-light: #d9d9dc;
    --silver-dark: #9fa0a4;
    --accent-red: #d0181f;
    --band-red-dark: #4a0c0f;
    --band-red: #9b2026;
    --brand-yellow: #f2ec1c;
    --box-edge: #e6e6e6;
  }
  * { margin: 0; padding: 0; box-sizing: border-box; }
  html, body {
    width: 1200px;
    height: 1200px;
    overflow: hidden;
    background: var(--page);
  }
  .canvas {
    position: relative;
    width: 1200px;
    height: 1200px;
    background: var(--page);
    font-family: "Signika", "Arial", sans-serif;
  }
  .label {
    position: absolute;
    left: 50px;
    top: 112px;
    width: 1100px;
    height: 975px;
    background: var(--label-black);
    overflow: hidden;
  }
  .silver-band {
    position: absolute;
    left: 0;
    width: 100%;
    background: linear-gradient(180deg, var(--silver-dark) 0%, var(--silver-light) 50%, var(--silver-dark) 100%);
  }
  .silver-band--top { top: 0; height: 63px; border-bottom: 4px solid var(--accent-red); }
  .silver-band--bottom { top: 872px; height: 103px; border-top: 4px solid var(--accent-red); }
  .mesh {
    position: absolute;
    left: 0;
    width: 100%;
    background: linear-gradient(90deg, var(--mesh-dark) 0%, var(--mesh-light) 50%, var(--mesh-dark) 100%);
  }
  .mesh--top { top: 67px; height: 161px; }
  .mesh--middle { top: 531px; height: 125px; }
  .mesh--lower { top: 802px; height: 70px; }
  .red-rule {
    position: absolute;
    left: 0;
    width: 100%;
    height: 5px;
    background: linear-gradient(90deg, var(--band-red-dark), var(--accent-red) 50%, var(--band-red-dark));
  }
  .red-rule--upper { top: 228px; }
  .red-rule--lower { top: 526px; }
  .brand-panel {
    position: absolute;
    left: 0;
    top: 233px;
    width: 100%;
    height: 293px;
    background: radial-gradient(ellipse at 75% 40%, var(--black-glow) 0%, var(--label-black) 65%);
    text-align: center;
  }
  .brand-name {
    position: absolute;
    left: 0;
    right: 0;
    top: 118px;
    font-size: 112px;
    font-weight: 700;
    line-height: 1;
    letter-spacing: 1px;
    color: var(--brand-yellow);
  }
  .brand-tagline {
    position: absolute;
    left: 0;
    right: 0;
    top: 241px;
    font-size: 24px;
    font-weight: 600;
    color: var(--brand-yellow);
  }
  .product-name {
    position: absolute;
    left: 309px;
    top: 548px;
    width: 482px;
    height: 60px;
    border: 2px solid var(--box-edge);
    border-top: none;
    border-radius: 0 0 10px 10px;
    background: var(--label-black);
    color: var(--brand-yellow);
    font-size: 40px;
    font-weight: 600;
    letter-spacing: 1px;
    line-height: 56px;
    text-align: center;
  }
  .facts-band {
    position: absolute;
    left: 0;
    top: 656px;
    width: 100%;
    height: 146px;
    background: linear-gradient(90deg, var(--band-red-dark) 0%, var(--band-red) 30%, var(--band-red) 70%, var(--band-red-dark) 100%);
    display: flex;
    flex-direction: column;
    justify-content: center;
    align-items: center;
    gap: 4px;
  }
  .facts-band li {
    list-style: none;
    color: var(--brand-yellow);
    font-size: 22px;
    font-weight: 500;
    line-height: 28px;
  }
</style>
</head>
<body>
<div class="canvas">
  <div class="label">
    <div class="silver-band silver-band--top"></div>
    <div class="mesh mesh--top" role="img" aria-label="Perforated dark metal texture band"></div>
    <div class="red-rule red-rule--upper"></div>

    <div class="brand-panel">
      <div class="brand-name">TelMO</div>
      <div class="brand-tagline">Shaping Stronger Bodies</div>
    </div>

    <div class="red-rule red-rule--lower"></div>
    <div class="mesh mesh--middle" role="img" aria-label="Perforated dark metal texture band"></div>
    <div class="product-name">POWER NUTRITION</div>

    <ul class="facts-band">
      <li>1 000 GRAM</li>
      <li>2 5 GRAM OF PROTEIN PER SERVING</li>
      <li>1 3 3 KCAL PER SERVING</li>
      <li>LOW CARBS</li>
    </ul>

    <div class="mesh mesh--lower" role="img" aria-label="Perforated dark metal texture band"></div>
    <div class="silver-band silver-band--bottom"></div>
  </div>
</div>
</body>
</html>
```